Brightfern Development Corporation
Can I please see design #42 with the symbols to designate the Phone, Fax, Email and Address? Thanks.
I also like the back of the business card on design 43-45.
I like the cards that do not have too much red and over power the business card. I do like the symbols to designate phone, fax, email, address and the website information. I would like some color on the card though. I do not like the cards that are all white.
The logo should be uploaded now. Off to a good start, but please don't forget the stationary. We are looking for letterhead, envelopes, etc.

```html
<!DOCTYPE html>
<html lang="en">
<head>
<meta charset="utf-8">
<title>Brightfern Development Corporation – Business Card</title>
<link rel="stylesheet" href="https://fonts.googleapis.com/css2?family=Open+Sans:wght@400;600;700;800&display=swap">
<style>
  :root {
    --backdrop: #2b2b2b;
    --card: #ffffff;
    --brand-red: #e8412c;
    --ink: #4a4a4a;
    --ink-dark: #333333;
    --band-dark: #4b4b4b;
    --divider: #cfcfcf;
  }
  * { margin: 0; padding: 0; box-sizing: border-box; }
  html, body {
    width: 1200px; height: 780px; overflow: hidden;
    background: var(--backdrop);
    font-family: "Open Sans", Arial, sans-serif;
  }
  .business-card {
    position: absolute; left: 100px; top: 104px;
    width: 1000px; height: 572px;
    background: var(--card);
    border-radius: 34px;
    overflow: hidden;
  }
  .brand-block {
    position: absolute; left: 58px; top: 210px;
    width: 340px;
    display: flex; align-items: flex-start; gap: 16px;
  }
  .brand-square {
    flex: none; width: 40px; height: 40px;
    background: var(--brand-red); margin-top: 6px;
  }
  .brand-name {
    font-weight: 800; color: var(--ink-dark);
    font-size: 31px; line-height: 1.12;
    text-transform: uppercase;
  }
  .column-divider {
    position: absolute; left: 422px; top: 36px;
    width: 2px; height: 400px;
    background: linear-gradient(to bottom, transparent, var(--divider) 15%, var(--divider) 85%, transparent);
  }
  .contact-column { position: absolute; left: 448px; top: 50px; }
  .person-name {
    color: var(--brand-red); font-weight: 700; font-size: 36px; line-height: 1.1;
  }
  .person-title { color: var(--ink); font-size: 20px; margin-top: 2px; }
  .contact-list { list-style: none; margin-top: 42px; }
  .contact-item {
    display: flex; align-items: flex-start; gap: 14px;
    color: var(--ink); font-size: 20px; line-height: 1.3;
    margin-bottom: 8px;
  }
  .contact-item.address { margin-bottom: 28px; }
  .contact-icon { flex: none; width: 20px; height: 20px; margin-top: 3px; fill: var(--brand-red); }
  .bottom-band { position: absolute; left: 0; bottom: 0; width: 1000px; height: 110px; }
  .band-red { fill: var(--brand-red); }
  .band-dark { fill: var(--band-dark); }
</style>
</head>
<body>
  <main class="business-card">
    <div class="brand-block">
      <span class="brand-square"></span>
      <span class="brand-name">Brightfern Development Corporation</span>
    </div>

    <div class="column-divider"></div>

    <section class="contact-column">
      <h1 class="person-name">Daniel Reyes</h1>
      <p class="person-title">Vice President</p>
      <ul class="contact-list">
        <li class="contact-item address">
          <svg class="contact-icon" viewBox="0 0 20 20"><path d="M10 1 L19 10 H16 V19 H12 V13 H8 V19 H4 V10 H1 Z"/></svg>
          <span>4180 Cedar Hollow Drive<br>Maple Ridge, CO 80412</span>
        </li>
        <li class="contact-item">
          <svg class="contact-icon" viewBox="0 0 20 20"><path d="M4 2 L8 2 L9 7 L6.5 8.5 C7.5 11 9 12.5 11.5 13.5 L13 11 L18 12 L18 16 C18 17 17 18 16 18 C8.5 18 2 11.5 2 4 C2 3 3 2 4 2 Z"/></svg>
          <span>(303) 555-0147</span>
        </li>
        <li class="contact-item">
          <svg class="contact-icon" viewBox="0 0 20 20"><path d="M5 1 H13 L15 3 V7 H5 Z M2 8 H18 V17 H2 Z M5 11 H8 V13 H5 Z M11 11 H15 V13 H11 Z"/></svg>
          <span>(303) 555-0182</span>
        </li>
        <li class="contact-item">
          <svg class="contact-icon" viewBox="0 0 20 20"><path d="M10 1 A9 9 0 1 0 16 17 L15 15.5 A7 7 0 1 1 17 10 V11 A1.5 1.5 0 0 1 14 11 V6 H12 V7 A4 4 0 1 0 13 13 A3.3 3.3 0 0 0 19 11 V10 A9 9 0 0 0 10 1 Z M10 8 A2 2 0 1 1 10 12 A2 2 0 1 1 10 8 Z"/></svg>
          <span>dreyes@brightferndevelopment.net</span>
        </li>
        <li class="contact-item">
          <svg class="contact-icon" viewBox="0 0 20 20"><path d="M10 1 A9 9 0 1 0 10 19 A9 9 0 1 0 10 1 Z M10 3 C11.5 4.5 12.3 6.5 12.5 9 H7.5 C7.7 6.5 8.5 4.5 10 3 Z M7.5 11 H12.5 C12.3 13.5 11.5 15.5 10 17 C8.5 15.5 7.7 13.5 7.5 11 Z M3.1 9 A7 7 0 0 1 7.3 3.5 C6.2 5 5.6 7 5.5 9 Z M14.5 9 C14.4 7 13.8 5 12.7 3.5 A7 7 0 0 1 16.9 9 Z M3.1 11 H5.5 C5.6 13 6.2 15 7.3 16.5 A7 7 0 0 1 3.1 11 Z M14.5 11 H16.9 A7 7 0 0 1 12.7 16.5 C13.8 15 14.4 13 14.5 11 Z"/></svg>
          <span>www.brightferndevelopment.net</span>
        </li>
      </ul>
    </section>

    <svg class="bottom-band" viewBox="0 0 1000 110" preserveAspectRatio="none" aria-hidden="true">
      <path class="band-red" d="M0 70 C250 92 550 96 800 66 L1000 40 V110 H0 Z"/>
      <path class="band-dark" d="M790 110 L800 78 C860 70 930 58 1000 44 V110 Z"/>
    </svg>
  </main>
</body>
</html>
```